Postcard Flyer For Plumbing Company

We are a p[professional plumbing company in NSW that carry out plumbing, electrical and hot water system work.
i want to send a postcard size flyer 105mm x 148mm to our clients to offer $xx off their next job they book with us.
The front of the flyer needs to say.... Feel The Love WIth $35 Off your Next Job. It needs to include a section where their name and postal address can go (74mm W x 24mm H) on the left hand side of the bottom of the flyer - refer attached example.
The other side of the flyer needs to have a section for text, the offer ($35 or $xx what they get off their next job) and also can use the tag line... Call 1 Number for The Best In 3 Trades - Plumbing, Hot Water & Electrical.
Plumbing, hot water and electrical pictures/icons can be used.
I want the flyer to stand out, use the corporate colours and be modern whilst letting them know that they can use this voucher on their next job.
Refer attachments.

Target Market(s)

Homeowners and our existing clients

Industry/Entity Type

Plumbing

Font styles to use
Serif

Colors
0255a3
ec1f27
ffffff
d3d3d3

Requirements
Must have
• Corporate colours and logos
• Red Colour:
• C=0
• M=100
• Y=100
• K=0
• Blue Colour
• C= 100
• M=66
• Y=0
• K=2
• Grey Colour
• C= 26
• M=21
• Y=19
• K=0
Nice to have
• predominately white background
Should not have
• Black background and lots of black.

```html
<!DOCTYPE html>
<html lang="en">
<head>
<meta charset="utf-8">
<title>Harlow Contracting – Postcard Flyer</title>
<link href="https://fonts.googleapis.com/css2?family=Oswald:wght@600;700&family=Montserrat:wght@700;800&family=Questrial&family=Roboto:wght@500;700&display=swap" rel="stylesheet">
<style>
  :root{
    --blue:#0255a3;
    --red:#ec1f27;
    --white:#ffffff;
    --grey:#d3d3d3;
    --stage:#8c8c8c;
    --ink:#1d1d1d;
  }
  *{box-sizing:border-box;margin:0;padding:0}
  html,body{width:943px;height:1200px;overflow:hidden;background:var(--stage)}
  .canvas{position:relative;width:943px;height:1200px}
  .card{position:absolute;left:101px;width:742px;height:523px;overflow:hidden;background:var(--white)}
  .card--front{top:51px}
  .card--back{top:627px}
  .card-art{position:absolute;inset:0;width:742px;height:523px}

  .brand{position:absolute;text-align:center}
  .brand-name{font-family:'Oswald',sans-serif;font-weight:700;color:var(--blue);line-height:.95;letter-spacing:1px;text-transform:uppercase}
  .brand-services{font-family:'Roboto',sans-serif;font-weight:500;font-size:12px;color:var(--ink);margin-top:8px;white-space:nowrap}

  /* front */
  .card--front .brand{left:522px;top:34px;width:206px}
  .card--front .brand-name{font-size:34px}
  .offer{position:absolute;right:25px;top:142px;text-align:right;font-family:'Oswald',sans-serif;font-weight:700;text-transform:uppercase}
  .offer-lead{font-size:31px;color:var(--blue);letter-spacing:1px;line-height:1}
  .offer-lead .accent{color:var(--red)}
  .offer-amount{font-size:78px;color:var(--red);line-height:1;margin-top:2px}
  .offer-tail{font-size:41px;color:var(--blue);letter-spacing:1px;line-height:1}
  .address-panel{position:absolute;left:0;top:405px;width:371px;height:118px;background:var(--white)}
  .intro{position:absolute;left:432px;top:420px;width:290px;font-family:'Questrial',sans-serif;font-size:17px;line-height:22px;color:var(--white);white-space:nowrap}
  .quote-mark{position:absolute;font-family:'Oswald',sans-serif;font-weight:700;font-size:44px;color:var(--white);line-height:1}
  .quote-open{left:392px;top:410px}
  .quote-close{left:656px;top:478px}

  /* back */
  .card--back .brand{left:34px;top:36px;width:188px}
  .card--back .brand-name{font-size:31px}
  .call{position:absolute;left:49px;top:306px;font-family:'Montserrat',sans-serif;font-weight:800;color:var(--white);font-size:62px;line-height:1}
  .tagline{position:absolute;left:49px;top:374px;font-family:'Montserrat',sans-serif;font-weight:800;color:var(--white);font-size:30.5px;line-height:1;white-space:nowrap;letter-spacing:.3px}
  .trades{position:absolute;left:0;top:418px;width:742px;height:52px;list-style:none}
  .trade{position:absolute;top:0;display:flex;align-items:center;gap:18px;font-family:'Roboto',sans-serif;font-weight:700;font-size:21px;color:var(--white)}
  .trade svg{width:52px;height:52px}
  .trade--plumbing{left:49px}
  .trade--hotwater{left:291px}
  .trade--electrical{left:531px}
  .contact-web{position:absolute;left:42px;top:486px;display:flex;align-items:center;gap:14px;font-family:'Roboto',sans-serif;font-weight:700;font-size:24px;letter-spacing:3px;color:var(--white)}
  .contact-phone{position:absolute;left:480px;top:483px;display:flex;align-items:center;gap:18px;font-family:'Roboto',sans-serif;font-weight:700;font-size:31px;color:var(--blue)}
</style>
</head>
<body>
<main class="canvas">

  <!-- Front of postcard -->
  <section class="card card--front">
    <svg class="card-art" viewBox="0 0 742 523" xmlns="http://www.w3.org/2000/svg">
      <defs>
        <linearGradient id="frontPhoto" x1="0" y1="0" x2="1" y2="0">
          <stop offset="0" stop-color="#c9a58f"/>
          <stop offset=".45" stop-color="#d9d3cd"/>
          <stop offset="1" stop-color="#f5f3f1"/>
        </linearGradient>
      </defs>
      <rect x="0" y="0" width="742" height="405" fill="url(#frontPhoto)" role="img" aria-label="Photo of a plumber in a red cap working on pipes under a bath"/>
      <path d="M0 322 C200 290 440 300 742 372 L742 523 L0 523 Z" fill="var(--blue)"/>
      <path d="M0 343 C200 312 440 322 742 392 L742 523 L0 523 Z" fill="var(--white)"/>
      <path d="M0 352 C200 322 440 332 742 400 L742 523 L0 523 Z" fill="var(--red)"/>
      <rect class="quote-panel" x="371" y="405" width="371" height="118" fill="var(--red)"/>
      <g stroke="var(--grey)" stroke-width="5">
        <circle cx="126" cy="296" r="79" fill="#8e9fb5" role="img" aria-label="Photo of a smiling plumber fixing a pipe"/>
        <circle cx="349" cy="330" r="67" fill="#d8dde2" role="img" aria-label="Photo of a chrome tap with running water"/>
        <circle cx="546" cy="360" r="52" fill="#b48a5a" role="img" aria-label="Photo of coloured electrical wires and cutters"/>
      </g>
      <g fill="none" stroke="var(--blue)" stroke-width="2">
        <circle cx="126" cy="296" r="82"/>
        <circle cx="349" cy="330" r="70"/>
        <circle cx="546" cy="360" r="55"/>
      </g>
    </svg>

    <div class="brand">
      <div class="brand-name">Harlow<br>Contracting</div>
      <div class="brand-services">Plumbing • Electrical • Hot Water</div>
    </div>

    <div class="offer">
      <div class="offer-lead">Feel the love <span class="accent">with</span></div>
      <div class="offer-amount">$35 Off</div>
      <div class="offer-tail">Your next job</div>
    </div>

    <div class="address-panel" aria-label="Recipient name and postal address"></div>

    <span class="quote-mark quote-open">“</span>
    <p class="intro">We are a professional plumbing<br>company in NSW that carry out<br>plumbing, electrical and<br>hot water system work</p>
    <span class="quote-mark quote-close">”</span>
  </section>

  <!-- Back of postcard -->
  <section class="card card--back">
    <svg class="card-art" viewBox="0 0 742 523" xmlns="http://www.w3.org/2000/svg">
      <defs>
        <linearGradient id="backPhoto" x1="0" y1="0" x2="1" y2="0">
          <stop offset="0" stop-color="#f6f6f6"/>
          <stop offset=".55" stop-color="#e6e8ea"/>
          <stop offset=".8" stop-color="#7d93b3"/>
          <stop offset="1" stop-color="#dcdcdc"/>
        </linearGradient>
      </defs>
      <rect x="0" y="0" width="742" height="340" fill="url(#backPhoto)" role="img" aria-label="Photo of a tradesman holding red and blue cables in a white kitchen"/>
      <rect x="0" y="0" width="250" height="135" fill="var(--white)" opacity=".85"/>
      <path d="M0 132 C160 140 320 200 430 292 C560 310 660 290 742 248 L742 523 L0 523 Z" fill="var(--red)"/>
      <path d="M0 164 C160 172 310 222 400 300 C520 326 640 318 742 276 L742 523 L0 523 Z" fill="var(--white)"/>
      <path d="M0 174 C160 182 300 232 390 310 C520 336 640 328 742 284 L742 523 L0 523 Z" fill="var(--blue)"/>
      <g stroke="var(--grey)" stroke-width="5">
        <circle cx="160" cy="208" r="79" fill="#9b7a5c" role="img" aria-label="Photo of hands tightening a fitting with a wrench"/>
        <circle cx="276" cy="268" r="62" fill="#a0703f" role="img" aria-label="Photo of a chrome hot water tap handle"/>
        <circle cx="396" cy="285" r="56" fill="#6c7a52" role="img" aria-label="Photo of a multimeter testing a switchboard"/>
      </g>
      <g fill="none" stroke="var(--blue)" stroke-width="2">
        <circle cx="160" cy="208" r="82"/>
        <circle cx="276" cy="268" r="65"/>
        <circle cx="396" cy="285" r="59"/>
      </g>
      <path d="M0 477 L430 477 L456 523 L0 523 Z" fill="var(--red)"/>
      <path d="M430 477 L742 477 L742 523 L456 523 Z" fill="var(--white)"/>
    </svg>

    <div class="brand">
      <div class="brand-name">Harlow<br>Contracting</div>
      <div class="brand-services">Plumbing • Electrical • Hot Water</div>
    </div>

    <h2 class="call">CALL</h2>
    <p class="tagline">1 NUMBER FOR THE BEST IN 3 TRADES</p>

    <ul class="trades">
      <li class="trade trade--plumbing">
        <svg viewBox="0 0 52 52" fill="none" stroke="var(--white)" stroke-width="1.6" aria-hidden="true">
          <circle cx="26" cy="26" r="24.5"/>
          <path d="M18 35 L30 23 M28 17 a6 6 0 1 0 7 7 l-3-3 -1-3 3-1 z" stroke-linejoin="round"/>
        </svg>
        Plumbing
      </li>
      <li class="trade trade--hotwater">
        <svg viewBox="0 0 52 52" fill="none" stroke="var(--white)" stroke-width="1.6" aria-hidden="true">
          <circle cx="26" cy="26" r="24.5"/>
          <path d="M14 24 H38 V30 a4 4 0 0 1 -4 4 H18 a4 4 0 0 1 -4 -4 Z M18 20 q2-2 0-4 M26 20 q2-2 0-4 M34 20 q2-2 0-4"/>
        </svg>
        Hot Water
      </li>
      <li class="trade trade--electrical">
        <svg viewBox="0 0 52 52" fill="none" stroke="var(--white)" stroke-width="1.6" aria-hidden="true">
          <circle cx="26" cy="26" r="24.5"/>
          <path d="M26 15 a7 7 0 0 1 4 12.7 V31 H22 V27.7 A7 7 0 0 1 26 15 Z M22 34 H30 M23 37 H29 M16 16 l2 2 M36 16 l-2 2 M26 10 v2"/>
        </svg>
        Electrical
      </li>
    </ul>

    <div class="contact-web">
      <svg width="20" height="20" viewBox="0 0 20 20" fill="none" stroke="var(--white)" stroke-width="1.5" aria-hidden="true">
        <circle cx="10" cy="10" r="8.5"/><ellipse cx="10" cy="10" rx="3.5" ry="8.5"/><path d="M1.5 10 H18.5 M3 5.5 H17 M3 14.5 H17"/>
      </svg>
      www.harlowtrades.com
    </div>
    <div class="contact-phone">
      <svg width="30" height="30" viewBox="0 0 30 30" fill="none" stroke="var(--blue)" stroke-width="2" aria-hidden="true">
        <path d="M7 4 l5 5 -3 3 q3 6 9 9 l3-3 5 5 -3 3 q-12 0 -19-13 Z" stroke-linejoin="round"/>
        <path d="M18 5 a7 7 0 0 1 7 7 M18 1 a11 11 0 0 1 11 11"/>
      </svg>
      015 480 3171
    </div>
  </section>

</main>
</body>
</html>
```